Price Calculator as Responsive Web App to support Sales People

We need to build a simple micro web app to support sales people in making quotes. We already have a backend that can take a number of parameters and create a quote. We need put a responsive web app on top of this so that our people on the road can easily do their price simulations.

We need two pages. One for the input and another for the results. No menus, navigations, etc. It is 6 different inputs as shown with boxes in the sketch. They don't need to be boxed, but some of them have a bit of instruction text that clearly need to belong to the input.

This needs to be responsive, but first and foremost designed for smartphones. I have included a background gradient that we would like to use -- or a variant of it. We expect this to be delivered as HTML/CSS + images so that we can quickly write a few pieces of JavaScript ourselves to wire it up to our price simulator.

Industry/Entity Type

Information Technology

Coding

Coded - Design and coding required

Number of Pages Required

2 page

Font styles to use
Sans Serif

Requirements
Must have
• Responsive design
• Easy to wire up JavaScript to the HTML/CSS
Nice to have
• Some quick way to pick number of months. +/- buttons to add remove a year or 3 months. Same thing with number of items. Add 10 or 5 quickly.
• Maybe some parallax effect while scrolling as long as it is not distracting.
Should not have
• Toolbars, Menus, Navigations, Banners, etc. This is just a single micro app.

```html
<!DOCTYPE html>
<html lang="en">
<head>
<meta charset="utf-8">
<title>Price Calculator</title>
<link href="https://fonts.googleapis.com/css2?family=Montserrat:wght@300;400;600;700;800&display=swap" rel="stylesheet">
<style>
:root{
  --page-bg:#2c2d3a;
  --panel-bg:#e6f4fd;
  --panel-white:#ffffff;
  --divider:#c3ccd4;
  --navy:#0a4c85;
  --blue:#0096ff;
  --deep-blue:#03528a;
  --amber:#ffc000;
  --track:#ffffff;
  --option-bg:#cfdde6;
  --option-border:#bccdd8;
  --option-text:#9fadb8;
  --option-light:#e9e9e9;
  --option-light-border:#dcdcdc;
  --option-light-text:#b4b4b4;
  --note:#7d8a94;
  --info:#b7cff0;
}
*{box-sizing:border-box;margin:0;padding:0}
html,body{width:1200px;height:837px;overflow:hidden}
body{background:var(--page-bg);font-family:'Montserrat',sans-serif;position:relative}
.calculator{position:absolute;left:312px;top:22px;width:577px;height:777px;background:var(--panel-bg);border-radius:2px;overflow:hidden}
.abs{position:absolute}
.range-label{font-weight:700;font-size:15px;color:var(--navy);transform:translateY(-50%)}
.track{height:8px;background:var(--track);border-radius:1px;transform:translateY(-50%);box-shadow:inset 0 0 0 1px #e2e8ee}
.track-fill{height:8px;background:var(--amber);transform:translateY(-50%)}
.knob{width:32px;height:32px;border-radius:50%;background:#fff;box-shadow:0 1px 4px rgba(0,0,0,.15);transform:translate(-50%,-50%);display:flex;align-items:center;justify-content:center}
.knob::after{content:"";width:16px;height:16px;border-radius:50%;background:var(--blue)}
.bubble{width:80px;height:32px;background:var(--blue);color:#fff;font-size:7px;font-weight:800;display:flex;align-items:center;justify-content:center;border-radius:1px;letter-spacing:-.1px}
.max-value{font-weight:800;font-size:32px;color:var(--navy);transform:translateY(-50%);line-height:1}
.max-unit{font-weight:400;font-size:12px;color:var(--navy);transform:translateY(-50%)}
.divider{left:0;width:577px;height:1px;background:var(--divider)}
.group-title{font-weight:400;font-size:12px;color:var(--navy);transform:translateY(-50%)}
.option{display:flex;flex-direction:column;align-items:center;justify-content:center;background:var(--option-bg);border:1px solid var(--option-border);color:var(--option-text);font-size:11px;font-weight:700;text-align:center;line-height:1.45}
.option small{font-size:11px;font-weight:300}
.option-light{background:var(--option-light);border-color:var(--option-light-border);color:var(--option-light-text)}
.note{display:flex;align-items:center;gap:9px;font-size:9.5px;font-weight:400;color:var(--note);line-height:1.35}
.note svg{flex:none}
.white-block{top:523px;height:174px;background:var(--panel-white);border:1px solid var(--divider)}
.action{top:697px;height:80px;display:flex;align-items:center;justify-content:center;color:#fff;font-weight:800;font-size:11px}
</style>
</head>
<body>
<main class="calculator">
  <!-- Duration -->
  <span class="abs range-label" style="left:17px;top:82px">Duration</span>
  <div class="abs track" style="left:90px;top:82px;width:366px"></div>
  <div class="abs track-fill" style="left:90px;top:82px;width:276px"></div>
  <div class="abs knob" style="left:366px;top:82px"></div>
  <div class="abs bubble" style="left:326px;top:26px">18 MONTHS</div>
  <span class="abs max-value" style="left:465px;top:82px">24</span>
  <span class="abs max-unit" style="left:511px;top:82px">Months</span>

  <!-- Count -->
  <span class="abs range-label" style="left:21px;top:173px">Count</span>
  <div class="abs track" style="left:83px;top:173px;width:365px"></div>
  <div class="abs track-fill" style="left:83px;top:173px;width:167px"></div>
  <div class="abs knob" style="left:250px;top:173px"></div>
  <div class="abs bubble" style="left:210px;top:117px">6 ITEMS</div>
  <span class="abs max-value" style="left:465px;top:173px">10</span>
  <span class="abs max-unit" style="left:517px;top:173px">Items</span>

  <div class="abs divider" style="top:199px"></div>

  <!-- Engine power -->
  <span class="abs group-title" style="left:16px;top:234px">Engine Power (Beyond Standard)</span>
  <div class="abs option" style="left:18px;top:258px;width:131px;height:65px">$360 per year<small>(Bronze Power)</small></div>
  <div class="abs option" style="left:155px;top:258px;width:131px;height:65px">$600 per year<small>(Silver Power)</small></div>
  <div class="abs option" style="left:291px;top:258px;width:131px;height:65px">$1M per year<small>(Gold Power)</small></div>
  <div class="abs option" style="left:427px;top:258px;width:131px;height:65px">$3M per year<small>(Platinum Power)</small></div>
  <p class="abs note" style="left:16px;top:334px;width:530px">
    <svg width="15" height="15" viewBox="0 0 15 15"><circle cx="7.5" cy="7.5" r="7" fill="#d6e6fa" stroke="var(--info)"/><rect x="7" y="6" width="1" height="5" fill="#fff"/><circle cx="7.5" cy="4.3" r=".8" fill="#fff"/></svg>
    <span>A basic engine Lorem ipsum dolor sit amet, consectetur adipiscing elit. Suspendisse varius enim in eros elementum tristique.</span>
  </p>

  <div class="abs divider" style="top:369px"></div>

  <!-- Shared storage -->
  <span class="abs group-title" style="left:16px;top:404px">Shared Storage Addition</span>
  <div class="abs option" style="left:22px;top:428px;width:98px;height:48px">10 KG</div>
  <div class="abs option" style="left:130px;top:428px;width:98px;height:48px">50 KG</div>
  <div class="abs option" style="left:239px;top:428px;width:98px;height:48px">100 KG</div>
  <div class="abs option" style="left:348px;top:428px;width:98px;height:48px">500 KG</div>
  <div class="abs option" style="left:458px;top:428px;width:98px;height:48px">1 TON</div>
  <p class="abs note" style="left:16px;top:487px;width:530px">
    <svg width="15" height="15" viewBox="0 0 15 15"><circle cx="7.5" cy="7.5" r="7" fill="#d6e6fa" stroke="var(--info)"/><rect x="7" y="6" width="1" height="5" fill="#fff"/><circle cx="7.5" cy="4.3" r=".8" fill="#fff"/></svg>
    <span>A basic engine Lorem ipsum dolor sit amet, consectetur adipiscing elit. Suspendisse varius enim in eros elementum tristique.</span>
  </p>

  <!-- Tip -->
  <section class="abs white-block" style="left:0;width:289px">
    <span class="abs group-title" style="left:16px;top:35px">Additional Tip</span>
    <div class="abs option option-light" style="left:20px;top:58px;width:77px;height:48px">15%</div>
    <div class="abs option option-light" style="left:105px;top:58px;width:77px;height:48px">18%</div>
    <div class="abs option option-light" style="left:190px;top:58px;width:77px;height:48px">20%</div>
    <p class="abs note" style="left:16px;top:123px;width:250px">
      <svg width="15" height="15" viewBox="0 0 15 15"><circle cx="7.5" cy="7.5" r="7" fill="#d6e6fa" stroke="var(--info)"/><rect x="7" y="6" width="1" height="5" fill="#fff"/><circle cx="7.5" cy="4.3" r=".8" fill="#fff"/></svg>
      <span>A basic engine Lorem ipsum dolor sit amet, consectetur adipiscing elit. Suspendisse varius enim in eros elementum tristique.</span>
    </p>
  </section>

  <!-- Elastic -->
  <section class="abs white-block" style="left:288px;width:289px">
    <span class="abs group-title" style="left:16px;top:35px">Elastic Extension</span>
    <div class="abs option option-light" style="left:22px;top:58px;width:115px;height:48px">30%</div>
    <div class="abs option option-light" style="left:150px;top:58px;width:115px;height:48px">50%</div>
    <p class="abs note" style="left:16px;top:123px;width:250px">
      <svg width="15" height="15" viewBox="0 0 15 15"><circle cx="7.5" cy="7.5" r="7" fill="#d6e6fa" stroke="var(--info)"/><rect x="7" y="6" width="1" height="5" fill="#fff"/><circle cx="7.5" cy="4.3" r=".8" fill="#fff"/></svg>
      <span>A basic engine Lorem ipsum dolor sit amet, consectetur adipiscing elit. Suspendisse varius enim in eros elementum tristique.</span>
    </p>
  </section>

  <!-- Actions -->
  <div class="abs action" style="left:0;width:288px;background:var(--deep-blue)"></div>
  <button class="abs action" style="left:288px;width:289px;background:var(--blue);border:0;font-family:inherit">GET QUOTE</button>
</main>
</body>
</html>
```